Custom Office Whiteboard for Staff

I need a custom whiteboard layout design. All fields are contained in the attached images along with artwork requirements including required bleed. Size will be 1200mm x 900mm.

Feel free to make is more visually appealing than this draft.

Use colors blue, black and white to keep company feel.

Font styles to use
Sans Serif

Colors
ffffff
000000
33a6d7

```html
<!DOCTYPE html>
<html lang="en">
<head>
<meta charset="utf-8">
<title>Skyward Ballooning – Staff Whiteboard</title>
<link href="https://fonts.googleapis.com/css2?family=Roboto+Condensed:wght@400;700&family=Roboto:wght@400;500;700&display=swap" rel="stylesheet">
<style>
:root{
  --navy:#0d2a47;
  --black:#000000;
  --white:#ffffff;
  --blue:#33a6d7;
  --row:#dde8f4;
  --line:#a6b0bc;
  --notes:#fdeeea;
}
*{box-sizing:border-box;margin:0;padding:0}
html,body{width:1200px;height:900px;overflow:hidden;background:var(--white)}
.board{position:relative;width:1200px;height:900px;overflow:hidden;background:var(--white);font-family:"Roboto",sans-serif}
.hero-photo{position:absolute;left:0;top:0;width:760px;height:104px;background:linear-gradient(180deg,#8a8f6a 0%,#6f7d3e 45%,#3f5424 100%)}
.shapes{position:absolute;left:0;top:0}
.brand{position:absolute;left:892px;top:18px;width:270px;height:74px;background:#0a0f18;display:flex;align-items:center;justify-content:center;gap:10px;
  font-family:"Roboto Condensed",sans-serif;font-weight:700;font-size:34px;color:var(--blue)}
.brand .dot{width:18px;height:18px;border-radius:50%;background:var(--blue)}
.panel{position:absolute}
table{border-collapse:collapse;width:100%;table-layout:fixed}
th,td{border:1px solid var(--line);text-align:center;overflow:hidden;white-space:nowrap}
.title th{background:var(--navy);color:var(--white);font-family:"Roboto Condensed",sans-serif;font-weight:700;border-color:var(--navy)}
.head th{background:var(--navy);color:var(--white);font-family:"Roboto Condensed",sans-serif;font-weight:400;border-color:#3a5674}
tbody tr:nth-child(odd) td{background:var(--row)}
tbody tr:nth-child(even) td{background:var(--white)}
.crew{left:66px;top:134px;width:673px}
.crew .title th{height:28px;font-size:17px}
.crew .head th{height:28px;font-size:12px;line-height:12px}
.crew td{height:28.3px}
.small td{font-size:10px;color:#111;height:23.2px}
.small .title th{height:23px;font-size:16px}
.small .head th{height:23px;font-size:12px}
.six{left:78px;top:550px;width:256px}
.twelve{left:346px;top:546px;width:257px}
.fleet{left:628px;top:545px;width:516px}
.fleet .title th{height:24px}
.notes{position:absolute;left:764px;top:136px;width:300px;height:396px;background:var(--notes);box-shadow:0 0 3px rgba(0,0,0,.25);
  font-family:"Roboto Condensed",sans-serif;font-weight:700;font-size:52px;text-align:center;padding-top:18px;color:var(--black)}
.footer{position:absolute;left:0;top:820px;width:1200px;color:var(--white);font-family:"Roboto Condensed",sans-serif;font-size:22px;text-align:center;line-height:28px}
.footer span{margin:0 12px}
</style>
</head>
<body>
<div class="board">
  <div class="hero-photo" role="img" aria-label="Aerial photo of a hot air balloon over vineyards and farmland"></div>
  <svg class="shapes" width="1200" height="900" viewBox="0 0 1200 900" aria-hidden="true">
    <path d="M690 0 L1200 0 L1200 234 C1130 226 1090 218 1064 216 L1064 136 C900 122 800 80 690 0 Z" fill="var(--black)"/>
    <path d="M0 808 C250 772 700 768 960 788 C1100 760 1180 680 1200 575 L1200 900 L0 900 Z" fill="var(--blue)"/>
    <path d="M0 820 C300 790 700 792 1000 802 C1120 792 1180 745 1200 722 L1200 900 L0 900 Z" fill="var(--black)"/>
  </svg>
  <div class="brand"><span class="dot"></span>Skyward</div>

  <div class="panel crew">
    <table>
      <thead>
        <tr class="title"><th colspan="9">Flight / Ground Crew</th></tr>
        <tr class="head"><th>Crew Name</th><th>License Class</th><th>Medical</th><th>BFR</th><th>Instructoor<br>Rating</th><th>CAO 20.11</th><th>DAMP</th><th>Maintenance<br>Authori</th><th>ASIC</th></tr>
      </thead>
      <tbody>
        <tr><td></td><td></td><td></td><td></td><td></td><td></td><td></td><td></td><td></td></tr>
        <tr><td></td><td></td><td></td><td></td><td></td><td></td><td></td><td></td><td></td></tr>
        <tr><td></td><td></td><td></td><td></td><td></td><td></td><td></td><td></td><td></td></tr>
        <tr><td></td><td></td><td></td><td></td><td></td><td></td><td></td><td></td><td></td></tr>
        <tr><td></td><td></td><td></td><td></td><td></td><td></td><td></td><td></td><td></td></tr>
        <tr><td></td><td></td><td></td><td></td><td></td><td></td><td></td><td></td><td></td></tr>
        <tr><td></td><td></td><td></td><td></td><td></td><td></td><td></td><td></td><td></td></tr>
        <tr><td></td><td></td><td></td><td></td><td></td><td></td><td></td><td></td><td></td></tr>
        <tr><td></td><td></td><td></td><td></td><td></td><td></td><td></td><td></td><td></td></tr>
        <tr><td></td><td></td><td></td><td></td><td></td><td></td><td></td><td></td><td></td></tr>
        <tr><td></td><td></td><td></td><td></td><td></td><td></td><td></td><td></td><td></td></tr>
        <tr><td></td><td></td><td></td><td></td><td></td><td></td><td></td><td></td><td></td></tr>
      </tbody>
    </table>
  </div>

  <div class="notes">NOTES</div>

  <div class="panel small six">
    <table>
      <thead>
        <tr class="title"><th colspan="2">6 Monthly Tasks</th></tr>
        <tr class="head"><th>Tasks</th><th>Due Date</th></tr>
      </thead>
      <tbody>
        <tr><td>Operations Manual</td><td></td></tr>
        <tr><td>Staff Meeting</td><td></td></tr>
        <tr><td>SMS Meeting</td><td></td></tr>
        <tr><td>Fire Extinguisher Inspection</td><td></td></tr>
        <tr><td>Flight Instrument Inspection</td><td></td></tr>
        <tr><td></td><td></td></tr>
        <tr><td></td><td></td></tr>
        <tr><td></td><td></td></tr>
      </tbody>
    </table>
  </div>

  <div class="panel small twelve">
    <table>
      <thead>
        <tr class="title"><th colspan="2">12 Monthly Tasks</th></tr>
        <tr class="head"><th>Tasks</th><th>Due Date</th></tr>
      </thead>
      <tbody>
        <tr><td>COA Internal Audit</td><td></td></tr>
        <tr><td>SMS Audit</td><td></td></tr>
        <tr><td>Fatigue Training</td><td></td></tr>
        <tr><td>CAO 20.11</td><td></td></tr>
        <tr><td></td><td></td></tr>
        <tr><td></td><td></td></tr>
        <tr><td></td><td></td></tr>
        <tr><td></td><td></td></tr>
      </tbody>
    </table>
  </div>

  <div class="panel small fleet">
    <table>
      <thead>
        <tr class="title"><th colspan="4">II Balloon Annual / Periodic Schedule</th></tr>
        <tr class="head"><th>Ballo</th><th>Type</th><th>Annual Date</th><th>Periodic Time</th></tr>
      </thead>
      <tbody>
        <tr><td>VH-QKA</td><td>Aero D90</td><td></td><td></td></tr>
        <tr><td>VH-QKB</td><td>Aero E180</td><td></td><td></td></tr>
        <tr><td>VH-QKC</td><td>Aero E240</td><td></td><td></td></tr>
        <tr><td>VH-QKD</td><td>Aero B400</td><td></td><td></td></tr>
        <tr><td>VH-QKE</td><td>Aero G450</td><td></td><td></td></tr>
        <tr><td></td><td></td><td></td><td></td></tr>
        <tr><td></td><td></td><td></td><td></td></tr>
        <tr><td></td><td></td><td></td><td></td></tr>
      </tbody>
    </table>
  </div>

  <div class="footer">
    <p><span>Email: info@skywardballooning.com.au</span><span>Web: www.skywardballooning.com.au</span><span>Phone: 1300 555 019</span></p>
    <p><span>Southern Aerostats Pty Ltd T/A Skyward Ballooning</span><span>CASA AOC: S400918</span><span>Certificate of Approval: 9182</span></p>
  </div>
</div>
</body>
</html>
```